Healthcare IT company looking for business card design

We develop IT systems for healthcare that significantly reduces cost and improves quality.

We want a business card design that is professional and clean, and using the colors in our logo.

Target Market(s)

Doctors and decision makers in the healthcare industry

Industry/Entity Type

Healthcare

Contact Information for Business Card

It should include
Name and title, address, telephone

Tobias Vrenholt, CEO
+46 712 418257
tobias@kelvaro.se

Font styles to use
Serif

Colors
0355a3
ed282f

Requirements
Must have
• Clean design
• Professional feel
Nice to have
• N/A
Should not have
• N/A

```html
<!DOCTYPE html>
<html lang="en">
<head>
<meta charset="UTF-8">
<title>Kelvaro Business Card</title>
<link rel="stylesheet" href="https://fonts.googleapis.com/css2?family=Source+Sans+3:wght@400;600;700&display=swap">
<style>
  :root {
    --stage: #000000;
    --brand-red: #e3001b;
    --brand-blue: #0758a3;
    --ink-light: #ffffff;
    --card-radius: 52px;
  }
  * { margin: 0; padding: 0; box-sizing: border-box; }
  html, body {
    width: 1200px;
    height: 900px;
    overflow: hidden;
    background: var(--stage);
    font-family: "Source Sans 3", "Helvetica Neue", Arial, sans-serif;
    color: var(--ink-light);
  }
  .canvas { position: relative; width: 1200px; height: 900px; }

  .card { position: absolute; overflow: hidden; }
  .card-front {
    left: 116px; top: 275px; width: 477px; height: 294px;
    background: var(--brand-red);
    border-radius: 0 var(--card-radius) 0 var(--card-radius);
  }
  .card-back {
    left: 622px; top: 276px; width: 477px; height: 293px;
    background: var(--brand-blue);
    border-radius: var(--card-radius) 0 var(--card-radius) 0;
  }

  .wordmark {
    position: absolute;
    font-weight: 700;
    letter-spacing: -0.5px;
    line-height: 1;
    white-space: nowrap;
  }
  .card-front .wordmark { left: 34px; top: 38px; font-size: 80px; }
  .card-back .wordmark { right: 52px; top: 192px; font-size: 70px; }

  .name-rule {
    position: absolute; top: 164px; height: 1px; background: var(--ink-light);
  }
  .name-rule-left { left: 0; width: 250px; }
  .name-rule-right { left: 456px; width: 21px; }
  .holder {
    position: absolute; left: 256px; top: 152px;
    font-size: 17px; font-weight: 700; white-space: nowrap;
  }
  .holder .role { font-size: 12px; font-weight: 600; }

  .contact-list {
    position: absolute; right: 28px; top: 194px;
    list-style: none; text-align: right; font-size: 13.5px;
  }
  .contact-list li {
    display: flex; justify-content: flex-end; align-items: center;
    gap: 5px; height: 20px;
  }
  .contact-list .icon { width: 10px; height: 10px; fill: var(--ink-light); }
  .contact-list .address { margin-top: 6px; }
</style>
</head>
<body>
<main class="canvas">
  <section class="card card-front" aria-label="Business card front">
    <div class="wordmark">Kelvaro</div>
    <div class="name-rule name-rule-left"></div>
    <p class="holder">Tobias Vrenholt, <span class="role">CEO</span></p>
    <div class="name-rule name-rule-right"></div>
    <ul class="contact-list">
      <li>+46 712 418257
        <svg class="icon" viewBox="0 0 10 10" aria-hidden="true"><path d="M2.1 0.4 L3.6 2.4 L2.8 3.4 C3.4 4.8 5.2 6.6 6.6 7.2 L7.6 6.4 L9.6 7.9 L8.6 9.6 C4.4 9.4 0.6 5.6 0.4 1.4 Z"/></svg>
      </li>
      <li>tobias@kelvaro.se
        <svg class="icon" viewBox="0 0 10 10" aria-hidden="true"><path d="M0.5 2 H9.5 V8.4 H0.5 Z M1.2 2.6 L5 5.6 L8.8 2.6" fill="var(--ink-light)" stroke="var(--brand-red)" stroke-width="0.8"/></svg>
      </li>
      <li class="address">12345, Address Goes Here Country Name, 123456</li>
    </ul>
  </section>

  <section class="card card-back" aria-label="Business card back">
    <div class="wordmark">Kelvaro</div>
  </section>
</main>
</body>
</html>
```